Breakfast Briefings / Lunch & Learn

I would like to have a double sided flyer size 8x10 to display the breakfast briefing on one side and Lunch & Learn on the other side.

Header on each side to say
2018 Calendar Breakfast Briefing (on the breakfast side)
2018 Calendar Lunch & Learn (on the lunch side)

I have attached a copy of the files we would like to use.

Industry/Entity Type

Learn

Colors

Designer to choose colors to be used in the design.

```html
<!DOCTYPE html>
<html lang="en">
<head>
<meta charset="utf-8">
<title>2018 Calendar – Breakfast Briefings / Lunch &amp; Learn</title>
<link rel="stylesheet" href="https://fonts.googleapis.com/css2?family=Roboto:wght@300;400;500;700&family=Oswald:wght@400;500&family=Playfair+Display:wght@400&display=swap">
<style>
:root{
  --stage:#3a3a3a;
  --teal:#1a9aa6;
  --teal-dark:#137d88;
  --ink:#222629;
  --pink:#e0336b;
  --row:#e9eaec;
  --row-alt:#f2f3f4;
  --page-left:#f3f4f5;
}
*{box-sizing:border-box;margin:0;padding:0}
html,body{width:1200px;height:776px;overflow:hidden;background:var(--stage)}
body{position:relative;font-family:"Roboto",Arial,sans-serif;color:var(--ink)}
.page{position:absolute;top:78px;width:474px;height:594px;overflow:hidden}
.page--breakfast{left:91px;background:linear-gradient(160deg,#fafafa 0%,var(--page-left) 55%,#e6e8ea 100%)}
.page--lunch{left:608px;background:#fff}
.layer{position:absolute;left:0;top:0;width:474px;height:594px}

/* breakfast side */
.brand{position:absolute;left:0;width:474px;top:40px;text-align:center;font-weight:300;font-size:24px;letter-spacing:6px;color:#3a3f47}
.kicker{position:absolute;font-weight:500;font-size:10px;letter-spacing:2px;text-transform:uppercase;color:var(--teal-dark)}
.heading{position:absolute;font-weight:400;font-size:17px;line-height:17px;color:var(--ink)}
.rule{position:absolute;height:1px;background:var(--ink)}
.topic{font-size:4px;fill:#333}
.node-text{font-size:3.7px;font-weight:700;fill:#fff;text-anchor:middle}
.center-label{font-size:7.5px;fill:var(--ink);text-anchor:middle}

/* lunch side */
.year{position:absolute;left:0;width:474px;top:50px;text-align:center;font-family:"Playfair Display",serif;font-size:26px;line-height:32px;color:var(--teal-dark)}
.year-rule{position:absolute;left:142px;width:190px;height:1px;background:linear-gradient(90deg,transparent,var(--pink),transparent)}
.subtitle{position:absolute;left:0;width:474px;top:86px;display:flex;justify-content:center;align-items:center;gap:8px;font-size:15px;line-height:16px;color:var(--ink)}
.sessions{position:absolute;left:87px;top:116px;width:300px;list-style:none;font-size:6.6px;color:#2c2f33}
.sessions li{display:flex;justify-content:space-between;height:12.4px;line-height:12.4px;padding:0 5px;background:var(--row);border-bottom:1px solid #fff}
.sessions li:nth-child(even){background:var(--row-alt)}

.badge{position:absolute;width:40px;height:40px;border-radius:50%;display:flex;align-items:center;justify-content:center;font-family:"Oswald",sans-serif;font-size:20px;color:#fff;box-shadow:0 0 0 4px #e4e6e8,2px 3px 6px rgba(0,0,0,.35)}
.month{position:absolute;width:48px}
.month h3{font-family:"Oswald",sans-serif;font-weight:400;font-size:6.5px;color:var(--pink);text-align:right;letter-spacing:.3px;margin-bottom:2px}
.days{display:grid;grid-template-columns:repeat(7,1fr);font-size:3.4px;line-height:5.2px;text-align:center;color:#444}
.days b{font-weight:700;color:#222}
.days i{font-style:normal}
.days i:first-of-type{grid-column-start:var(--s)}
</style>
</head>
<body>

<!-- Breakfast side -->
<section class="page page--breakfast" aria-label="2018 Calendar Breakfast Briefing">
  <svg class="layer" viewBox="0 0 474 594">
    <defs>
      <radialGradient id="saladTones" cx="55%" cy="45%" r="65%">
        <stop offset="0" stop-color="#9fbf6a"/>
        <stop offset=".45" stop-color="#d9dcd4"/>
        <stop offset="1" stop-color="#b9c2c6"/>
      </radialGradient>
      <filter id="soft" x="-20%" y="-20%" width="140%" height="140%"><feDropShadow dx="0" dy="1" stdDeviation="3" flood-opacity=".18"/></filter>
    </defs>

    <circle cx="120" cy="478" r="170" fill="var(--teal)"/>
    <circle cx="108" cy="482" r="158" fill="#fff"/>
    <circle cx="104" cy="485" r="147" fill="url(#saladTones)" role="img" aria-label="Photo of fresh salad bowls on a buffet table"/>

    <g transform="translate(0 14)">
      <circle cx="310" cy="238" r="62" fill="#fff" filter="url(#soft)"/>
      <rect x="284" y="198" width="52" height="42" rx="6" fill="#1b1b1b" role="img" aria-label="Illustration of a lunch box with breakfast food"/>
      <text class="center-label" x="310" y="256">360 Breakfast Briefings</text>

      <g>
        <polygon points="306,158 313,162 306,166" fill="#f5a31a" transform="rotate(18 310 238)"/>
        <polygon points="306,158 313,162 306,166" fill="#c9dc1b" transform="rotate(54 310 238)"/>
        <polygon points="306,158 313,162 306,166" fill="#9ad31e" transform="rotate(90 310 238)"/>
        <polygon points="306,158 313,162 306,166" fill="#3cc13f" transform="rotate(126 310 238)"/>
        <polygon points="306,158 313,162 306,166" fill="#2fb84e" transform="rotate(162 310 238)"/>
        <polygon points="306,158 313,162 306,166" fill="#22c76a" transform="rotate(198 310 238)"/>
        <polygon points="306,158 313,162 306,166" fill="#2bc9a0" transform="rotate(234 310 238)"/>
        <polygon points="306,158 313,162 306,166" fill="#2ab8c0" transform="rotate(270 310 238)"/>
        <polygon points="306,158 313,162 306,166" fill="#2a9fd6" transform="rotate(306 310 238)"/>
        <polygon points="306,158 313,162 306,166" fill="#3a73c9" transform="rotate(342 310 238)"/>
      </g>

      <g>
        <circle cx="310" cy="150" r="18" fill="#f5a31a"/>
        <text class="node-text" x="310" y="145">Finance</text><text class="node-text" x="310" y="151">Rosa Calder</text><text class="node-text" x="310" y="157">March</text>
        <circle cx="364" cy="170" r="18" fill="#c9dc1b"/>
        <text class="node-text" x="364" y="165">R&amp;D</text><text class="node-text" x="364" y="171">Dean Arlow</text><text class="node-text" x="364" y="177">April</text>
        <circle cx="390" cy="212" r="18" fill="#9ad31e"/>
        <text class="node-text" x="390" y="207">Operations</text><text class="node-text" x="390" y="213">Paul Brenner</text><text class="node-text" x="390" y="219">May</text>
        <circle cx="390" cy="264" r="18" fill="#3cc13f"/>
        <text class="node-text" x="390" y="259">Clinical/Reg</text><text class="node-text" x="390" y="265">Mark Ellison</text><text class="node-text" x="390" y="271">June</text>
        <circle cx="360" cy="308" r="18" fill="#2fb84e"/>
        <text class="node-text" x="360" y="303">Quality</text><text class="node-text" x="360" y="309">Owen Radley</text><text class="node-text" x="360" y="315">July</text>
        <circle cx="311" cy="324" r="18" fill="#22c76a"/>
        <text class="node-text" x="311" y="319">Medical</text><text class="node-text" x="311" y="325">Luke Fenwick</text><text class="node-text" x="311" y="331">August</text>
        <circle cx="262" cy="308" r="18" fill="#2bc9a0"/>
        <text class="node-text" x="262" y="303">Marketing</text><text class="node-text" x="262" y="309">Ravi K. Mehta</text><text class="node-text" x="262" y="315">September</text>
        <circle cx="231" cy="262" r="18" fill="#2ab8c0"/>
        <text class="node-text" x="231" y="257">Legal</text><text class="node-text" x="231" y="263">Omar Saleh</text><text class="node-text" x="231" y="269">October</text>
        <circle cx="231" cy="212" r="18" fill="#2a9fd6"/>
        <text class="node-text" x="231" y="207">Market Access</text><text class="node-text" x="231" y="213">Karen Holt</text><text class="node-text" x="231" y="219">November</text>
        <circle cx="262" cy="170" r="18" fill="#3a73c9"/>
        <text class="node-text" x="262" y="165">TOS</text><text class="node-text" x="262" y="171">Nina Hale</text><text class="node-text" x="262" y="177">December</text>
      </g>

      <g>
        <text class="topic" x="334" y="141">• Finance for Non-Finance People</text>
        <text class="topic" x="334" y="147">• Budgets</text>
        <text class="topic" x="388" y="163">• Topic: TBD</text>
        <text class="topic" x="414" y="211">• Topic: TBD</text>
        <text class="topic" x="414" y="261">• Topic: TBD</text>
        <text class="topic" x="384" y="312">• Topic: TBD</text>
        <text class="topic" x="328" y="350">• Topic: TBD</text>
        <text class="topic" x="240" y="306" text-anchor="end">• Topic: TBD</text>
        <text class="topic" x="210" y="267" text-anchor="end">• Topic: TBD</text>
        <text class="topic" x="210" y="210" text-anchor="end">• Topic: TBD</text>
        <text class="topic" x="240" y="162" text-anchor="end">• Topic: TBD</text>
        <text class="topic" x="404" y="345">2019 Sales / People</text>
      </g>
    </g>

    <g fill="none" stroke="var(--teal)" stroke-width="1.6" stroke-linecap="round">
      <path d="M40 92 c-3 4 3 6 0 10"/>
      <path d="M31 103 h18 v6 a9 9 0 0 1 -18 0 z" fill="var(--teal)" stroke="none"/>
      <path d="M49 106 h3 a3 3 0 0 1 0 6 h-4"/>
      <path d="M28 120 h24"/>
    </g>
  </svg>

  <div class="brand">CORVANA</div>

  <div class="kicker" style="left:62px;top:96px">2018 Calendar</div>
  <div class="rule" style="left:0;top:116px;width:28px"></div>
  <div class="heading" style="left:62px;top:111px">Breakfast</div>
  <div class="heading" style="left:107px;top:128px">Briefings</div>
  <div class="rule" style="left:170px;top:137px;width:76px"></div>
</section>

<!-- Lunch & Learn side -->
<section class="page page--lunch" aria-label="2018 Calendar Lunch and Learn">
  <svg class="layer" viewBox="0 0 474 594">
    <defs>
      <linearGradient id="peopleTones" x1="0" y1="0" x2="1" y2="1">
        <stop offset="0" stop-color="#c9d6de"/>
        <stop offset=".55" stop-color="#8fa6b4"/>
        <stop offset="1" stop-color="#2d3338"/>
      </linearGradient>
    </defs>
    <path d="M0 0 H474 V16 C350 38 120 38 0 16 Z" fill="var(--teal)"/>
    <path d="M0 22 C120 44 350 44 474 22 V26 C350 48 120 48 0 26 Z" fill="#7cc9cf"/>
    <g transform="translate(0 22)">
      <path d="M0 594 V520 C40 440 190 385 474 412 V432 C230 408 80 450 26 594 Z" fill="var(--teal)"/>
      <path d="M26 594 C80 450 230 408 474 432 V594 Z" fill="url(#peopleTones)" role="img" aria-label="Photo of a business person touching a wall of team portraits"/>
    </g>
  </svg>

  <div class="year-rule" style="top:48px"></div>
  <div class="year">2018 Calendar</div>
  <div class="subtitle">
    <svg width="22" height="16" viewBox="0 0 22 16" aria-hidden="true" fill="var(--teal)">
      <circle cx="11" cy="2" r="2"/><path d="M2 13 a9 9 0 0 1 18 0 z"/><rect x="0" y="13.5" width="22" height="2" rx="1"/>
    </svg>
    <span>Lunch &amp; Learn</span>
  </div>
  <div class="year-rule" style="top:108px"></div>

  <ul class="sessions">
    <li><span>Mindfulness</span><span>3/22/2018</span></li>
    <li><span>Nutrition and Lifestyle Coaching</span><span>4/26/2018</span></li>
    <li><span>What is Neuromodulation?</span><span>5/15/2018</span></li>
    <li><span>Achieve Your Goals</span><span>6/20/2018</span></li>
    <li><span>Changing Your Life with Positive Thinking</span><span>7/18/2018</span></li>
    <li><span>What is Clean Eating and How Do I Get Started</span><span>Aug</span></li>
    <li><span>Budgeting 101 Financial Wellness</span><span>Sept</span></li>
    <li><span>Busted! Nutrition Myths</span><span>10/1/2018</span></li>
    <li><span>Time Management: No time like the present</span><span>11/1/2018</span></li>
    <li><span>1st Time Home Buyers</span><span>12/1/2018</span></li>
  </ul>

  <div class="badge" style="left:30px;top:258px;background:#1e9fd6">01</div>
  <div class="month" style="left:76px;top:254px"><h3>JANUARY</h3><div class="days" style="--s:2"><b>S</b><b>M</b><b>T</b><b>W</b><b>T</b><b>F</b><b>S</b><i>1</i><i>2</i><i>3</i><i>4</i><i>5</i><i>6</i><i>7</i><i>8</i><i>9</i><i>10</i><i>11</i><i>12</i><i>13</i><i>14</i><i>15</i><i>16</i><i>17</i><i>18</i><i>19</i><i>20</i><i>21</i><i>22</i><i>23</i><i>24</i><i>25</i><i>26</i><i>27</i><i>28</i><i>29</i><i>30</i><i>31</i></div></div>

  <div class="badge" style="left:135px;top:258px;background:#1aa89a">02</div>
  <div class="month" style="left:181px;top:254px"><h3>FEBRUARY</h3><div class="days" style="--s:5"><b>S</b><b>M</b><b>T</b><b>W</b><b>T</b><b>F</b><b>S</b><i>1</i><i>2</i><i>3</i><i>4</i><i>5</i><i>6</i><i>7</i><i>8</i><i>9</i><i>10</i><i>11</i><i>12</i><i>13</i><i>14</i><i>15</i><i>16</i><i>17</i><i>18</i><i>19</i><i>20</i><i>21</i><i>22</i><i>23</i><i>24</i><i>25</i><i>26</i><i>27</i><i>28</i></div></div>

  <div class="badge" style="left:241px;top:258px;background:#4cb748">03</div>
  <div class="month" style="left:287px;top:254px"><h3>MARCH</h3><div class="days" style="--s:5"><b>S</b><b>M</b><b>T</b><b>W</b><b>T</b><b>F</b><b>S</b><i>1</i><i>2</i><i>3</i><i>4</i><i>5</i><i>6</i><i>7</i><i>8</i><i>9</i><i>10</i><i>11</i><i>12</i><i>13</i><i>14</i><i>15</i><i>16</i><i>17</i><i>18</i><i>19</i><i>20</i><i>21</i><i>22</i><i>23</i><i>24</i><i>25</i><i>26</i><i>27</i><i>28</i><i>29</i><i>30</i><i>31</i></div></div>

  <div class="badge" style="left:346px;top:258px;background:#c6d22a">04</div>
  <div class="month" style="left:392px;top:254px"><h3>APRIL</h3><div class="days" style="--s:1"><b>S</b><b>M</b><b>T</b><b>W</b><b>T</b><b>F</b><b>S</b><i>1</i><i>2</i><i>3</i><i>4</i><i>5</i><i>6</i><i>7</i><i>8</i><i>9</i><i>10</i><i>11</i><i>12</i><i>13</i><i>14</i><i>15</i><i>16</i><i>17</i><i>18</i><i>19</i><i>20</i><i>21</i><i>22</i><i>23</i><i>24</i><i>25</i><i>26</i><i>27</i><i>28</i><i>29</i><i>30</i></div></div>

  <div class="badge" style="left:30px;top:310px;background:#f2b418">05</div>
  <div class="month" style="left:76px;top:306px"><h3>MAY</h3><div class="days" style="--s:3"><b>S</b><b>M</b><b>T</b><b>W</b><b>T</b><b>F</b><b>S</b><i>1</i><i>2</i><i>3</i><i>4</i><i>5</i><i>6</i><i>7</i><i>8</i><i>9</i><i>10</i><i>11</i><i>12</i><i>13</i><i>14</i><i>15</i><i>16</i><i>17</i><i>18</i><i>19</i><i>20</i><i>21</i><i>22</i><i>23</i><i>24</i><i>25</i><i>26</i><i>27</i><i>28</i><i>29</i><i>30</i><i>31</i></div></div>

  <div class="badge" style="left:135px;top:310px;background:#f08a1c">06</div>
  <div class="month" style="left:181px;top:306px"><h3>JUNE</h3><div class="days" style="--s:6"><b>S</b><b>M</b><b>T</b><b>W</b><b>T</b><b>F</b><b>S</b><i>1</i><i>2</i><i>3</i><i>4</i><i>5</i><i>6</i><i>7</i><i>8</i><i>9</i><i>10</i><i>11</i><i>12</i><i>13</i><i>14</i><i>15</i><i>16</i><i>17</i><i>18</i><i>19</i><i>20</i><i>21</i><i>22</i><i>23</i><i>24</i><i>25</i><i>26</i><i>27</i><i>28</i><i>29</i><i>30</i></div></div>

  <div class="badge" style="left:241px;top:310px;background:#e8402a">07</div>
  <div class="month" style="left:287px;top:306px"><h3>JULY</h3><div class="days" style="--s:1"><b>S</b><b>M</b><b>T</b><b>W</b><b>T</b><b>F</b><b>S</b><i>1</i><i>2</i><i>3</i><i>4</i><i>5</i><i>6</i><i>7</i><i>8</i><i>9</i><i>10</i><i>11</i><i>12</i><i>13</i><i>14</i><i>15</i><i>16</i><i>17</i><i>18</i><i>19</i><i>20</i><i>21</i><i>22</i><i>23</i><i>24</i><i>25</i><i>26</i><i>27</i><i>28</i><i>29</i><i>30</i><i>31</i></div></div>

  <div class="badge" style="left:346px;top:310px;background:#d3232f">08</div>
  <div class="month" style="left:392px;top:306px"><h3>AUGUST</h3><div class="days" style="--s:4"><b>S</b><b>M</b><b>T</b><b>W</b><b>T</b><b>F</b><b>S</b><i>1</i><i>2</i><i>3</i><i>4</i><i>5</i><i>6</i><i>7</i><i>8</i><i>9</i><i>10</i><i>11</i><i>12</i><i>13</i><i>14</i><i>15</i><i>16</i><i>17</i><i>18</i><i>19</i><i>20</i><i>21</i><i>22</i><i>23</i><i>24</i><i>25</i><i>26</i><i>27</i><i>28</i><i>29</i><i>30</i><i>31</i></div></div>

  <div class="badge" style="left:30px;top:362px;background:#e63b4a">09</div>
  <div class="month" style="left:76px;top:358px"><h3 style="text-align:left">SEPTEMBER</h3><div class="days" style="--s:7"><b>S</b><b>M</b><b>T</b><b>W</b><b>T</b><b>F</b><b>S</b><i>1</i><i>2</i><i>3</i><i>4</i><i>5</i><i>6</i><i>7</i><i>8</i><i>9</i><i>10</i><i>11</i><i>12</i><i>13</i><i>14</i><i>15</i><i>16</i><i>17</i><i>18</i><i>19</i><i>20</i><i>21</i><i>22</i><i>23</i><i>24</i><i>25</i><i>26</i><i>27</i><i>28</i><i>29</i><i>30</i></div></div>

  <div class="badge" style="left:135px;top:362px;background:#6b2f9c">10</div>
  <div class="month" style="left:181px;top:358px"><h3 style="text-align:left">OCTOBER</h3><div class="days" style="--s:2"><b>S</b><b>M</b><b>T</b><b>W</b><b>T</b><b>F</b><b>S</b><i>1</i><i>2</i><i>3</i><i>4</i><i>5</i><i>6</i><i>7</i><i>8</i><i>9</i><i>10</i><i>11</i><i>12</i><i>13</i><i>14</i><i>15</i><i>16</i><i>17</i><i>18</i><i>19</i><i>20</i><i>21</i><i>22</i><i>23</i><i>24</i><i>25</i><i>26</i><i>27</i><i>28</i><i>29</i><i>30</i><i>31</i></div></div>

  <div class="badge" style="left:241px;top:362px;background:#c8155a">11</div>
  <div class="month" style="left:287px;top:358px"><h3 style="text-align:left">NOVEMBER</h3><div class="days" style="--s:5"><b>S</b><b>M</b><b>T</b><b>W</b><b>T</b><b>F</b><b>S</b><i>1</i><i>2</i><i>3</i><i>4</i><i>5</i><i>6</i><i>7</i><i>8</i><i>9</i><i>10</i><i>11</i><i>12</i><i>13</i><i>14</i><i>15</i><i>16</i><i>17</i><i>18</i><i>19</i><i>20</i><i>21</i><i>22</i><i>23</i><i>24</i><i>25</i><i>26</i><i>27</i><i>28</i><i>29</i><i>30</i></div></div>

  <div class="badge" style="left:346px;top:362px;background:#a0208c">12</div>
  <div class="month" style="left:392px;top:358px"><h3>DECEMBER</h3><div class="days" style="--s:7"><b>S</b><b>M</b><b>T</b><b>W</b><b>T</b><b>F</b><b>S</b><i>1</i><i>2</i><i>3</i><i>4</i><i>5</i><i>6</i><i>7</i><i>8</i><i>9</i><i>10</i><i>11</i><i>12</i><i>13</i><i>14</i><i>15</i><i>16</i><i>17</i><i>18</i><i>19</i><i>20</i><i>21</i><i>22</i><i>23</i><i>24</i><i>25</i><i>26</i><i>27</i><i>28</i><i>29</i><i>30</i><i>31</i></div></div>
</section>

</body>
</html>
```